Tallowmoor Letterheads Design

Hello, we have just upgraded this project for a guaranteed payment.

We are currently going through a re-branding exercise internally. Our logo is attached as a PDF file.

We are happy with our logo but would like to investigate how we can best apply the logo to our letterheads and compliment slips.

We are a quality printing company in England. Despite our name we are very professional and offer a personal service.

Our new website is under construction and here is a link to show you how it looks: http://brackenpress.v4ntor.co.uk

The style must be professional and steer away from "tacky" otherwise it makes our company look very low budget and just a bit silly.

We would like to see elements of creativity though, so please, nothing too boring.

I have attached our new logo, there is an option for use on white or black.

Cheers
Tallowmoor Team

Reason: We have increased the deadline due to an internal delay to things, we now have more time before we need anything to be printed.

Industry/Entity Type

Construction

Requirements
Must have
• IMPORTANT! Please do not tweak or change our logo in any way. A few designs show vast changes in the logo, this is not what we require. Please do not change the logo in any way. Thanks
Nice to have
• Classy but approachable. Elements of "quirky" would be nice to see.
Should not have
• A Tacky feel

```html
<!DOCTYPE html>
<html lang="en">
<head>
<meta charset="utf-8">
<title>Tallowmoor – With Compliments Slip</title>
<link rel="stylesheet" href="https://fonts.googleapis.com/css2?family=Questrial&display=swap">
<style>
  :root {
    --ink: #1b1e20;
    --brand-pink: #e6317b;
    --paper: #ffffff;
    --cloud: #ffffff;
    --mist: #eeeeee;
    --heading: #1e1e1e;
  }
  * { margin: 0; padding: 0; box-sizing: border-box; }
  html, body {
    width: 1200px;
    height: 567px;
    overflow: hidden;
    background: var(--paper);
  }
  .slip {
    position: relative;
    width: 1200px;
    height: 567px;
    background: var(--paper);
    font-family: "Questrial", "Century Gothic", sans-serif;
    overflow: hidden;
  }
  .header-band {
    position: absolute;
    left: 0; top: 0;
    width: 1200px;
    height: 150px;
    background: var(--ink);
  }
  .brand {
    position: absolute;
    left: 24px;
    top: 18px;
    width: 200px;
  }
  .brand-dot {
    display: block;
    width: 58px;
    height: 58px;
    margin-left: 62px;
    border-radius: 50%;
    background: var(--brand-pink);
  }
  .brand-name {
    display: block;
    margin-top: 6px;
    color: var(--paper);
    font-size: 33px;
    line-height: 1;
    letter-spacing: 0.2px;
  }
  .brand-tagline {
    display: block;
    margin-top: 6px;
    margin-left: 34px;
    color: var(--paper);
    font-size: 14px;
    letter-spacing: 0.3px;
  }
  .contact-cloud {
    position: absolute;
    right: 0;
    top: 0;
    width: 380px;
    height: 180px;
  }
  .contact-cloud path { fill: var(--cloud); }
  .contact {
    position: absolute;
    right: 26px;
    top: 14px;
    text-align: right;
    color: var(--brand-pink);
    font-size: 14px;
    line-height: 20px;
    list-style: none;
  }
  .contact .web { font-weight: 700; }
  .watermark {
    position: absolute;
    left: -60px;
    top: 170px;
    width: 620px;
    height: 460px;
    border-radius: 50%;
    background: radial-gradient(ellipse at 50% 45%, var(--mist) 0%, rgba(238,238,238,0.6) 55%, rgba(255,255,255,0) 72%);
  }
  .slip-title {
    position: absolute;
    left: 0;
    top: 160px;
    width: 1200px;
    text-align: center;
    color: var(--heading);
    font-size: 31px;
    font-weight: 400;
    letter-spacing: 0.5px;
  }
</style>
</head>
<body>
  <main class="slip">
    <div class="header-band"></div>

    <div class="brand">
      <span class="brand-dot"></span>
      <span class="brand-name">Tallowmoor</span>
      <span class="brand-tagline">Quality Printing</span>
    </div>

    <svg class="contact-cloud" viewBox="0 0 380 180" aria-hidden="true">
      <path d="M40 0 H380 V150
               C360 172 330 172 312 158
               C296 176 262 178 246 160
               C226 178 190 176 178 156
               C158 172 124 170 116 148
               C92 156 66 142 66 118
               C40 118 22 96 34 76
               C12 66 8 38 30 26
               C22 16 28 4 40 0 Z"/>
    </svg>

    <ul class="contact">
      <li>• 12 Mill Lane, Ashcombe-On-The-Wold,</li>
      <li>Ashcombe, Kent, TN9 4QE</li>
      <li>• Tel: 0208 734 0529</li>
      <li class="web">• www.brackenpress.v4ntor.co.uk</li>
    </ul>

    <div class="watermark" role="img" aria-label="Large faint brand decoration in pale grey"></div>

    <h1 class="slip-title">WITH COMPLIMENTS</h1>
  </main>
</body>
</html>
```